ecommerce website design for pool store

I need a homepage designed for an e-commerce store for a pool shop. It will be similar to https://www.aquabrite.com.au/ but not an exact copy (ie. the icons, photos and colour scheme need to be different). aquabrite.com.au is one of our competitors but we love everything about their website.
I have attached the logo for this site. We want the background to be white and the colours used on the site to be the blue from the logo and the blue and green used on www.hopscotchyouth.com.au
I want the same layout for the logo, search and menu bar at the top along with the 'shop filter cartidges' feature button
Under that a similar slideshow
Under that, the categories with the logos, the best sellers, trending now (but call this 'latest products') and all the other same elements as on this example site.

```html
<!DOCTYPE html>
<html lang="en">
<head>
<meta charset="utf-8">
<title>Poolside Depot</title>
<link href="https://fonts.googleapis.com/css2?family=Montserrat:wght@400;500;600;700&display=swap" rel="stylesheet">
<style>
:root{
  --blue:#1766c2;
  --blue-dark:#0f4f9e;
  --green:#a3c62a;
  --ink:#2b2b2b;
  --muted:#666;
  --line:#d9dde3;
  --nav-bg:#eef0f4;
  --white:#fff;
}
*{box-sizing:border-box;margin:0;padding:0}
html,body{width:1200px;height:2899px;overflow:hidden;background:var(--white)}
body{font-family:'Montserrat',sans-serif;color:var(--ink);position:relative}
.abs{position:absolute}
.topbar{left:0;top:0;width:1200px;height:18px;background:var(--blue);color:#fff;font-size:9px}
.topbar span{position:absolute;top:4px}
.topbar i{display:inline-block;width:10px;height:8px;background:#fff;border-radius:2px;margin-right:6px;vertical-align:-1px}
.header{left:0;top:18px;width:1200px;height:52px;background:#fff}
.search{left:424px;top:32px;width:392px;height:24px;border:1px solid #9aa;font-size:9px;color:#777;padding:6px 10px}
.search-btn{left:792px;top:32px;width:24px;height:24px;background:var(--green)}
.filter-btn{left:825px;top:31px;width:150px;height:25px;background:#2a9ad6;color:#fff;font-size:11.5px;font-weight:600;text-align:center;line-height:25px}
.nav{left:0;top:70px;width:1200px;height:27px;background:var(--nav-bg)}
.nav a{position:absolute;top:8px;font-size:10px;color:var(--ink);text-decoration:none;font-weight:500}
.store-name{display:flex;align-items:center;gap:8px;color:var(--blue);font-weight:600;white-space:nowrap}
.store-name b{display:inline-block;border-radius:50%;background:var(--blue)}
.hero{left:0;top:97px;width:1200px;height:469px;background:linear-gradient(180deg,#b98f86 0%,#8a7f8a 22%,#5d7a8f 45%,#2f7fb0 65%,#1f5f8a 100%)}
.hero h1{position:absolute;left:0;width:1200px;top:140px;text-align:center;color:#fff;font-size:41px;font-weight:600}
.hero p{position:absolute;left:300px;width:600px;top:199px;text-align:center;color:#fff;font-size:12.5px;font-weight:500;line-height:18px}
.hero .cta{position:absolute;left:522px;top:263px;width:156px;height:36px;background:var(--green);color:#fff;font-size:18px;font-weight:500;text-align:center;line-height:36px}
.brand{top:622px;font-size:15px;font-weight:600;color:var(--blue-dark);display:flex;align-items:center;gap:6px}
.brand b{display:inline-block;width:14px;height:14px;border-radius:50%;background:var(--blue)}
.cat{height:58px;border:1px solid var(--blue);background:#fff;box-shadow:0 2px 4px rgba(0,0,0,.15)}
.cat span{position:absolute;left:20px;top:21px;font-size:12.5px;font-weight:500}
.cat i{position:absolute;right:16px;top:6px;width:62px;height:44px;border-radius:6px}
.section-title{left:227px;font-size:26px;font-weight:600}
.rule{left:225px;width:750px;height:1px;background:var(--blue)}
.card{width:169px;height:277px;border:1px solid var(--line);background:#fff}
.card .img{position:absolute;left:14px;top:14px;width:140px;height:122px;border-radius:4px}
.card .name{position:absolute;left:15px;top:158px;font-size:12px;font-weight:500;line-height:15px;width:145px}
.card .name em{font-style:normal;font-weight:400;color:#444}
.card .price{position:absolute;left:15px;top:199px;font-size:11.5px;color:#444}
.card .add{position:absolute;left:15px;top:235px;width:137px;height:24px;background:var(--green);color:#fff;font-size:10.5px;font-weight:500;text-align:center;line-height:24px}
.arrow{font-size:30px;color:var(--blue);font-weight:500}
.promo-img{left:225px;top:1787px;width:750px;height:327px;background:linear-gradient(120deg,#2aa6c9 0%,#e93d9c 35%,#f3a3c4 60%,#2a7fa6 100%)}
.promo-card{left:634px;top:1825px;width:306px;height:333px;background:#fff;box-shadow:0 2px 10px rgba(0,0,0,.18)}
.feat-title{font-size:12.5px;font-weight:500;left:92px}
.feat-text{font-size:8.6px;color:#555;line-height:15px;left:92px;width:185px}
.feat-icon{left:24px;width:44px;height:36px}
.footer-line{left:0;top:2228px;width:1200px;height:2px;background:#8ba0b8}
.f-about{left:365px;top:2286px;width:220px;font-size:9px;color:#444;line-height:15px}
.f-h{font-size:12.5px;font-weight:500}
.f-input{border:1px solid #bbb;font-size:9px;color:#666;padding:6px 8px;height:24px}
.col-h{top:2543px;font-size:9.5px;font-weight:600}
.col a{display:block;font-size:9px;color:#444;text-decoration:none;margin-bottom:10px}
.pay{top:2574px;width:32px;height:20px;border-radius:2px}
.social{top:2812px;width:14px;height:14px;border-radius:50%;background:#1d3a6a}
.copy{left:0;width:1200px;top:2849px;text-align:center;font-size:9px;color:#444}
</style>
</head>
<body>

<div class="abs topbar">
  <span style="left:226px"><i></i>Free Shipping</span>
  <span style="left:346px"><i></i>Buy Now, Pay Later, PayNext</span>
  <span style="left:524px"><i></i>60 Day Easy Returns</span>
  <span style="left:893px"><i style="width:8px;border-radius:50%"></i>Login</span>
  <span style="left:948px"><i></i>0</span>
</div>

<div class="abs header"></div>
<div class="abs store-name" style="left:182px;top:35px;font-size:16px"><b style="width:14px;height:14px"></b>Poolside Depot</div>
<div class="abs search">Search...</div>
<div class="abs search-btn">
  <svg width="24" height="24" viewBox="0 0 24 24"><circle cx="11" cy="11" r="5" fill="none" stroke="#fff" stroke-width="2"/><path d="M15 15l4 4" stroke="#fff" stroke-width="2"/></svg>
</div>
<div class="abs filter-btn">Shop Filter Cartridges</div>

<nav class="abs nav">
  <a style="left:327px">Pumps</a>
  <a style="left:396px">Filters</a>
  <a style="left:460px">Chlorinators</a>
  <a style="left:552px">Cleaners</a>
  <a style="left:628px">Lights</a>
  <a style="left:692px">Maintenance</a>
  <a style="left:787px">Heaters</a>
  <a style="left:859px">Covers</a>
  <a style="left:926px">Chemicals</a>
</nav>

<section class="abs hero" role="img" aria-label="Infinity pool on a hillside terrace at sunset with wooden deck and lounge chairs">
  <h1>Lorem Ipsum Dolor</h1>
  <p>Consectetuer adipiscing elit, sed diam nonummy nibh euismod tincidunt ut laoreet dolore magna aliquam erat volutpat.</p>
  <div class="cta">Shop Now</div>
</section>

<div class="abs brand" style="left:236px"><b></b>Tidewell</div>
<div class="abs brand" style="left:404px"><b></b>Northfrost</div>
<div class="abs brand" style="left:553px"><b></b>Shoreline</div>
<div class="abs brand" style="left:712px"><b></b>PureDose</div>
<div class="abs brand" style="left:880px"><b></b>Ironback</div>

<div class="abs cat" style="left:225px;top:711px;width:234px"><span>Pumps ›</span><i role="img" aria-label="Pool pump" style="background:#3c4a52"></i></div>
<div class="abs cat" style="left:225px;top:769px;width:234px"><span>Chlorinators ›</span><i role="img" aria-label="Salt chlorinator" style="background:#8b9096"></i></div>
<div class="abs cat" style="left:225px;top:826px;width:234px"><span>Filters ›</span><i role="img" aria-label="Filter cartridge" style="background:#cfe0ee;width:30px;right:40px"></i></div>
<div class="abs cat" style="left:482px;top:711px;width:235px"><span>Cleaners ›</span><i role="img" aria-label="Pool cleaner" style="background:#2e6fa8"></i></div>
<div class="abs cat" style="left:482px;top:769px;width:235px"><span>Lights ›</span><i role="img" aria-label="Pool light" style="background:#c9ccd4;border-radius:50%;width:46px;right:24px"></i></div>
<div class="abs cat" style="left:482px;top:826px;width:235px"><span>Pool Hoses ›</span><i role="img" aria-label="Coiled pool hose" style="background:#2b5f94;border-radius:50%;width:46px;right:24px"></i></div>
<div class="abs cat" style="left:740px;top:711px;width:235px"><span>Heaters ›</span><i role="img" aria-label="Pool heater" style="background:#4a4d52"></i></div>
<div class="abs cat" style="left:740px;top:769px;width:235px"><span>Spa Parts ›</span><i role="img" aria-label="Spa fittings" style="background:#dcdfe3"></i></div>
<div class="abs cat" style="left:740px;top:826px;width:235px"><span>Chemicals ›</span><i role="img" aria-label="Chemical bottle" style="background:#3c8fd8;width:22px;right:30px"></i></div>

<h2 class="abs section-title" style="top:944px">Best Sellers</h2>
<div class="abs rule" style="top:995px"></div>
<div class="abs arrow" style="left:172px;top:1136px">‹</div>
<div class="abs arrow" style="left:1010px;top:1136px">›</div>

<div class="abs card" style="left:225px;top:1021px"><div class="img" role="img" aria-label="Heat pump unit" style="background:#2c2d30"></div><div class="name">Pool Heat Pump<br><em>ThermaFlow 6KW</em></div><div class="price">$1299.99</div><div class="add">Add to Cart</div></div>
<div class="abs card" style="left:419px;top:1021px"><div class="img" role="img" aria-label="Pool cleaning kit" style="background:#bcd3ec"></div><div class="name">Pool Cleaning<br><em>5 in 1 Kit</em></div><div class="price">$299.99</div><div class="add">Add to Cart</div></div>
<div class="abs card" style="left:612px;top:1021px"><div class="img" role="img" aria-label="Pump and filter set" style="background:#2d6f73"></div><div class="name">Pool Pump and Filter with Housing</div><div class="price">$599.99</div><div class="add">Add to Cart</div></div>
<div class="abs card" style="left:807px;top:1021px"><div class="img" role="img" aria-label="White skimmer box" style="background:#e6e8ea"></div><div class="name">Pool Skim<br><em>White Standard</em></div><div class="price">$199.99</div><div class="add">Add to Cart</div></div>

<h2 class="abs section-title" style="top:1363px">Latest Products</h2>
<div class="abs rule" style="top:1414px"></div>
<div class="abs arrow" style="left:172px;top:1555px">‹</div>
<div class="abs arrow" style="left:1010px;top:1555px">›</div>

<div class="abs card" style="left:225px;top:1440px"><div class="img" role="img" aria-label="Algaecide bottle" style="background:#e3ece4"></div><div class="name">ClearTide<br>Algaecide 1 L</div><div class="price">$29.99</div><div class="add">Add to Cart</div></div>
<div class="abs card" style="left:419px;top:1440px"><div class="img" role="img" aria-label="Pump enclosure box" style="background:#2a2a2a"></div><div class="name">Acoustic Box Pump &amp; Filter Enclosure</div><div class="price">$2,999.99</div><div class="add">Add to Cart</div></div>
<div class="abs card" style="left:612px;top:1440px"><div class="img" role="img" aria-label="Bubble pool cover" style="background:linear-gradient(135deg,#8fb7bf,#4c7f88);left:0;top:0;width:167px;height:128px"></div><div class="name">Marigold Titanium Pool Cover</div><div class="price">$599.99</div><div class="add">Add to Cart</div></div>
<div class="abs card" style="left:807px;top:1440px"><div class="img" role="img" aria-label="Cartridge filter housing" style="background:#6f7c92"></div><div class="name">Cartridge Filter<br>Solstice</div><div class="price">$399.99</div><div class="add">Add to Cart</div></div>

<div class="abs promo-img" role="img" aria-label="Colourful inflatable pool floats and a flamingo ring on blue pool water"></div>
<div class="abs promo-card">
  <svg class="abs feat-icon" style="top:28px" viewBox="0 0 44 36"><rect x="1" y="6" width="28" height="20" rx="2" fill="var(--blue)"/><path d="M29 12h8l6 7v7H29z" fill="var(--blue)"/><circle cx="10" cy="29" r="4" fill="var(--blue)" stroke="#fff" stroke-width="2"/><circle cx="35" cy="29" r="4" fill="var(--blue)" stroke="#fff" stroke-width="2"/></svg>
  <div class="abs feat-title" style="top:33px">Free Shipping</div>
  <div class="abs feat-text" style="top:50px">Lorem ipsum dolor sit amet, consectetuer adipiscing elit sed diam nonummy nibh euismod tincidunt.</div>

  <svg class="abs feat-icon" style="top:120px;height:44px" viewBox="0 0 44 44"><rect x="4" y="2" width="36" height="14" rx="7" fill="var(--blue)"/><rect x="18" y="10" width="8" height="30" rx="4" fill="var(--blue)"/></svg>
  <div class="abs feat-title" style="top:119px">Buy Now, Pay Later, PayNext</div>
  <div class="abs feat-text" style="top:138px">Quis nostrud exerci tation ullamcorper suscipit lobortis nisl ut aliquip ex ea commodo consequat. Duis autem vel eum iriure dolor in hendrerit.</div>

  <svg class="abs feat-icon" style="top:230px;height:40px" viewBox="0 0 44 40"><path d="M22 2l18 8v20l-18 8-18-8V10z" fill="var(--blue)"/><path d="M4 10l18 8 18-8M22 18v20" stroke="#fff" stroke-width="2" fill="none"/></svg>
  <div class="abs feat-title" style="top:223px">60 Day Easy Returns</div>
  <div class="abs feat-text" style="top:242px">Vel illum dolore eu feugiat nulla facilisis at vero eros et accumsan et iusto odio dignissim qui blandit praesent luptatum zzril delenit augue.</div>
</div>

<div class="abs footer-line"></div>
<div class="abs store-name" style="left:226px;top:2314px;font-size:17px"><b style="width:16px;height:16px"></b>Poolside Depot</div>
<div class="abs f-about">Lorem ipsum dolor sit amet, consectetuer adipiscing elit sed.<br><br>Diam nonummy nibh euismod tincidunt. Quis nostrud exerci tation ullamcorper suscipit lobortis nisl ut aliquip ex ea commodo consequat.</div>

<div class="abs f-h" style="left:641px;top:2284px">What Are You Looking For?</div>
<div class="abs f-input" style="left:641px;top:2312px;width:334px">Search...</div>
<div class="abs search-btn" style="left:951px;top:2312px"><svg width="24" height="24" viewBox="0 0 24 24"><circle cx="11" cy="11" r="5" fill="none" stroke="#fff" stroke-width="2"/><path d="M15 15l4 4" stroke="#fff" stroke-width="2"/></svg></div>
<div class="abs f-h" style="left:641px;top:2374px">Signup for our Newsletter</div>
<div class="abs f-input" style="left:641px;top:2402px;width:260px">Email Address</div>
<div class="abs" style="left:899px;top:2402px;width:76px;height:24px;background:var(--green);color:#fff;font-size:11px;font-weight:600;text-align:center;line-height:24px">Signup</div>

<div class="abs" style="left:225px;top:2494px;width:750px;height:1px;background:#888"></div>

<div class="abs col-h" style="left:226px">Poolside Depot</div>
<div class="abs col" style="left:226px;top:2576px"><a>Pumps</a><a>Filters</a><a>Chlorinators</a><a>Cleaners</a><a>Lights</a><a>Maintenance</a><a>Heaters</a><a>Covers</a><a>Chemicals</a></div>
<div class="abs col-h" style="left:423px">About</div>
<div class="abs col" style="left:423px;top:2576px"><a>About us</a><a>Reviews</a><a>Blog</a><a>Free Quote</a></div>
<div class="abs col-h" style="left:585px">Support</div>
<div class="abs col" style="left:585px;top:2576px"><a>My Account</a><a>Contact Us</a><a>Manuals &amp; Forms</a><a>Careers</a><a>Sign Up For Our Catalog</a><a>Track Your Order</a></div>
<div class="abs col-h" style="left:797px">Secure payments with</div>
<div class="abs pay" style="left:797px;background:#2a4fa0"></div>
<div class="abs pay" style="left:844px;background:#333"></div>
<div class="abs pay" style="left:891px;background:#3a8fd6"></div>
<div class="abs pay" style="left:939px;background:#e9e9e9"></div>
<div class="abs" style="left:797px;top:2620px;font-size:9px;color:#444">Call us at</div>
<svg class="abs" style="left:797px;top:2641px" width="18" height="18" viewBox="0 0 18 18"><circle cx="9" cy="9" r="9" fill="var(--blue)"/><path d="M6 5l2 0 1 2-1 1a5 5 0 002 2l1-1 2 1v2a1 1 0 01-1 1A7 7 0 015 6a1 1 0 011-1z" fill="#fff"/></svg>
<div class="abs" style="left:826px;top:2641px;font-size:16px;font-weight:600;color:#1d2a40">1300 555 014</div>

<div class="abs" style="left:0;top:2819px;width:550px;height:1px;background:var(--blue)"></div>
<div class="abs" style="left:650px;top:2819px;width:550px;height:1px;background:var(--blue)"></div>
<div class="abs social" style="left:566px"></div>
<div class="abs social" style="left:590px"></div>
<div class="abs social" style="left:615px"></div>

<div class="abs copy">©2022. Poolside Depot. All Rights Reserved. Terms and Conditions. Privacy Policy</div>

</body>
</html>
```